Stationary for a Manufacturing Company focused on R&D
Twin-Kay please refer to the concluded Logo Project
Stationary for a Manufacturing Company focused on R&D - Manufacturing
Creative Brief
Use same font as used in my logo
Yes please refer to the log - keep the background colors simple
Modern
Vikram Talwarkar
Stationary for a Manufacturing company
Rustomji Parekh Building, 58 Hill Street, Fortm Mumbai 400019 India
vikram@twin-kay.com
www.twin-kay.com
The card must show advancement - something different but easy to duplicate.....
no information on the back - maybe just the logo at the back could be ok

```html
<!DOCTYPE html>
<html lang="en">
<head>
<meta charset="utf-8">
<title>Twin-Kay Stationery</title>
<link href="https://fonts.googleapis.com/css2?family=Open+Sans:wght@400;600&display=swap" rel="stylesheet">
<style>
  :root{
    --bg:#e9eaea;
    --paper:#ffffff;
    --green:#3d6b44;
    --green-dark:#2a4c30;
    --grey:#8a8f8c;
    --grey-light:#c9cccb;
    --ink:#4a4d4c;
    --shadow:0 3px 8px rgba(0,0,0,.18);
  }
  html,body{margin:0;padding:0;overflow:hidden}
  body{width:1200px;height:936px;background:var(--bg);position:relative;font-family:"Open Sans",sans-serif;color:var(--ink)}
  .sheet{position:absolute;background:var(--paper);box-shadow:var(--shadow);overflow:hidden}
  .wave{position:absolute;left:0;bottom:0;width:100%}

  .wordmark{font-family:"Open Sans",sans-serif;font-weight:600;color:var(--ink);display:flex;align-items:center;gap:.45em;white-space:nowrap;line-height:1}
  .mark-dot{display:inline-block;border-radius:50%;background:var(--green);flex:none}

  .web{position:absolute;left:0;width:100%;text-align:center;color:#fff;letter-spacing:.2em;font-size:11px;font-family:"Open Sans",sans-serif}

  .letterhead{left:178px;top:51px;width:411px;height:571px}
  .letterhead .wordmark{position:absolute;left:30px;top:42px;font-size:14px}
  .letterhead .mark-dot{width:16px;height:16px}
  .contact{position:absolute;left:262px;top:30px;font-size:7.5px;line-height:12px;margin:0;padding:0;list-style:none}
  .contact li::before{content:"";display:inline-block;width:5px;height:5px;border-radius:50%;background:var(--green);margin-right:5px}
  .letterhead .web{bottom:22px;font-size:10px}

  .folder{left:634px;top:46px;width:432px;height:576px}
  .folder .brand{position:absolute;left:0;top:220px;width:100%;display:flex;flex-direction:column;align-items:center;gap:14px}
  .folder .mark-dot{width:56px;height:56px}
  .folder .wordmark{font-size:28px}
  .folder .rule{width:200px;height:2px;background:var(--green)}
  .folder .web{bottom:26px}

  .card{left:46px;width:195px;height:89px}
  .card-front{top:723px}
  .card-front .wordmark{position:absolute;left:10px;top:13px;font-size:9px}
  .card-front .mark-dot{width:10px;height:10px}
  .card-front .details{position:absolute;left:112px;top:10px;font-size:5.5px;line-height:8px}
  .card-front .details b{color:var(--green);font-weight:600}
  .card-back{top:820px;background:linear-gradient(135deg,#5d8a63,var(--green-dark))}
  .card-back .wordmark{position:absolute;left:0;top:0;width:100%;height:100%;justify-content:center;color:#fff;font-size:11px}
  .card-back .mark-dot{width:13px;height:13px;background:#dfe8e0}

  .envelope{left:272px;top:718px;width:312px;height:190px}
  .envelope .wordmark{position:absolute;left:0;top:24px;width:100%;justify-content:center;font-size:9px}
  .envelope .mark-dot{width:10px;height:10px}
  .envelope .return{position:absolute;left:0;top:52px;width:100%;text-align:center;font-size:6.5px;line-height:10px}

  .envelope-back{left:629px;top:716px;width:437px;height:192px;background:#f4f5f4}
  .envelope-back .flap{position:absolute;left:0;top:0;width:100%;height:100%}
  .envelope-back .web{top:24px;font-size:9px}
</style>
</head>
<body>

<section class="sheet letterhead">
  <div class="wordmark"><span class="mark-dot"></span>Twin-Kay</div>
  <ul class="contact">
    <li>Rustomji Parekh Building</li>
    <li>58 Hill Street, Fortm</li>
    <li>Mumbai 400019 India</li>
    <li>Tel +91 22 5550 0101</li>
    <li>Fax +91 22 5550 0102</li>
    <li>vikram@twin-kay.com</li>
    <li>www.twin-kay.com</li>
  </ul>
  <svg class="wave" viewBox="0 0 411 80" height="80" preserveAspectRatio="none">
    <path d="M0 22 C110 -4 250 46 411 12" fill="none" stroke="var(--grey-light)" stroke-width="2"/>
    <path d="M0 30 C120 6 260 52 411 22" fill="none" stroke="var(--grey)" stroke-width="2"/>
    <path d="M0 38 C130 14 270 58 411 30 L411 80 L0 80Z" fill="var(--green)"/>
  </svg>
  <div class="web">www.twin-kay.com</div>
</section>

<section class="sheet folder">
  <div class="brand">
    <span class="mark-dot"></span>
    <div class="wordmark">Twin-Kay</div>
    <div class="rule"></div>
  </div>
  <svg class="wave" viewBox="0 0 432 90" height="90" preserveAspectRatio="none">
    <path d="M0 20 C120 -6 270 50 432 10" fill="none" stroke="var(--grey-light)" stroke-width="2"/>
    <path d="M0 30 C130 4 280 58 432 22" fill="none" stroke="var(--grey)" stroke-width="2"/>
    <path d="M0 40 C140 12 290 64 432 32 L432 90 L0 90Z" fill="var(--green)"/>
  </svg>
  <div class="web">www.twin-kay.com</div>
</section>

<section class="sheet card card-front">
  <div class="wordmark"><span class="mark-dot"></span>Twin-Kay</div>
  <div class="details">
    <b>Vikram Talwarkar</b><br>Director<br>Mob +91 98 5550 4477<br>vikram@twin-kay.com<br>www.twin-kay.com
  </div>
  <svg class="wave" viewBox="0 0 195 30" height="30" preserveAspectRatio="none">
    <path d="M0 12 C60 0 120 24 195 6" fill="none" stroke="var(--grey)" stroke-width="1.5"/>
    <path d="M0 18 C70 6 130 28 195 12 L195 30 L0 30Z" fill="var(--green)"/>
  </svg>
</section>

<section class="sheet card card-back">
  <div class="wordmark"><span class="mark-dot"></span>Twin-Kay</div>
</section>

<section class="sheet envelope">
  <div class="wordmark"><span class="mark-dot"></span>Twin-Kay</div>
  <div class="return">Rustomji Parekh Building, 58 Hill Street,<br>Fortm Mumbai 400019 India</div>
</section>

<section class="sheet envelope-back">
  <svg class="flap" viewBox="0 0 437 192" preserveAspectRatio="none">
    <path d="M0 0 H437 V70 C300 40 150 110 0 70Z" fill="var(--green)"/>
    <path d="M0 78 C150 118 300 48 437 78" fill="none" stroke="var(--grey)" stroke-width="2"/>
  </svg>
  <div class="web">www.twin-kay.com</div>
</section>

</body>
</html>
```